Snapvella needs You

Help us create an inviting, amazing, sleek, simple, clear landing page for a picture-memory-social connection site!

Business Name: SnapVella
Industry: Social Networking and Creativity through Pictures
A web platform for and about a community that is driven by a passion for sharing, caring, bonding, collaborating, creating and earning with pictures, through pictures and other related creative activities. This is going to be a great site for all creative artists-photographers, artists, graphic artists to express their work and their creativity.

The main focus of the site is - CONNECTIONS.
This will be uncoded.

Desired Website Screen Size
1024x768... Widescreen/Landscape orientation, is what we mean... So it fits on a CPU screen.

Desired look and feel and message
Look: Visitor should feel immersed in the page, in the world the page creates, simple, elegant, sophisticated, contemporary. We really like a clean uncluttered look.

Special mention: By the way we love the marketing genius who thought up this branding for pralu yogurt where they used the two dots above the o to create a branding effect that made this brand instantly identifiable. http://www.pralu.ca/en/

The two dots by themselves without having even the name present brings up the whole brand now. The dots are used above all the ingredients of the yogurt creating friendly figures, and above people in commercials-bringing the people onto the side of "team" pralu. Snapvella may have a character created or something distinctive in the letters in the name created to brand the site as well.

Feel: Engaging; Magical without being corny, here is a link to give an example look and feel but please do not be hindered in your creativity by this suggestion. We love all creative angles.
http://artscrapbin.com/graphic/5830261-camera-film-roll-blue-background

Message: Life and memories and connections through pictures.

Target audience:
The site is focused on pictures but not confined to photography enthusiasts (although they are an integral part of the site). Customers/Visitors will include families, corporates and the younger generation - all age groups, all class, everyone with pictures to express, memories to share.

Website design we like:
http://varnomdesign.com/work/northern-choral-guild/
http://varnomdesign.com/work/bitsprout/

What colors do we want to see on our landing page?
We would like the background to be grey or blue since it is grey is picture neutral colour and blue highlights pictures well and we also like blue and silver, which can be integrated into the theme. Also like green. But please do not let these instructions limit your creativity. We are open to new ideas and colours.

Predetermined Concepts if any:
We have a concept in mind and we think it would be cool to have an interface for the user through the back of a camera on the landing page -This could be used to create a scene or world the visitor feels a part of or is immersed into. The back screen of the camera may act as a screen for the slideshow of featured pictures on the site.

Content on the Page:
Photo Gallery with full screen, thumbnail view, zoom option etc.
Prominent but short introductory message
Sign in / Login Options
Links: Home Page; About; Info/Help; Contact Us; Privacy Policy; Terms of Use
At the bottom of the page: Follow Me/Like/Workmesh...social buttons.

Please feel free to add any other element to the landing page that you think might add to the effect of simple yet amazing look -clean, simple, uncluttered, sophisticated, stylish, inviting and engaging.
The concept is a guideline, but we would like you to be as creative as you can, even if it meant stepping out of these guidelines - rethink design, style, content if you like. We believe in bringing a solution in an innovative yet simple and elegant style. Something a visitor would be intrigued enough to explore and the guest would feel comfortable enough taking that step forward to have fun on the site. If you believe in the same, and you have the skill then you will have what we need. Good luck, go for it and we are excited to see what the amazing designers on this amazing site have to offer.
If you have any questions please free to ask.
Updates

HI wanted to send an update that this project design has been guaranteed.

Our site will be one to celebrate and showcase imagination as well as connection.  We would love to see what you create. Keep in mind our site will showcase all creativity, photographs, artists, graphic artists so this would be a benefit you may want to take advantage of in the future, a place where, if you so choose, you could gain exposure for your work. Therefore, even if you do not win the design project there is possible future benefit.

Imagination is everything.
Imagination encircles the world.-Holberg

Reason: We are giving the designers who accepted invites but have not yet submitted a chance to finish their submissions and the ones who are working on revisions a chance to finish those:)

Hello everyone,

Due to time constraints we must come to a decision sooner than the deadline of 28th. 

So, please try to submit any new designs or modifications to the old ones before the 26th. We are very thankful to all of you who have participated - for your designs, enthusiasm and kind words. 

Good luck! :)

• Thank you for the interest shown and your submissions! Designers who have submitted up until now have shown great potential. We are VERY excited with the quality of work and designs.

We want to add that Snapvella is not exclusively for the photographers. The site is for every person who may have a picture to store, organise, use or share - whether publicly or with only a few friends and family.

Snapvella is about allowing people to take control of their creativity. It is about providing tools to our users so that they can build their own connections and social network... of friends, family, fans, clients, ideas, thoughts, emotions etc. through pictures without worrying about their privacy or control over their creations.

With this update we want to encourage others to go beyond the camera theme. Do not let us restrict your creativity. Let YOUR OWN ideas take over if that’s what you think will best convey the message and will appeal to the users.

```html
<!DOCTYPE html>
<html lang="en">
<head>
<meta charset="utf-8">
<title>SnapVella</title>
<link href="https://fonts.googleapis.com/css2?family=Signika:wght@400;600&family=Source+Sans+3:wght@400;600&display=swap" rel="stylesheet">
<style>
:root{
  --bg:#2b2b2b;
  --halo:#363636;
  --body-dark:#1c1d20;
  --body-mid:#2a2c30;
  --bezel:#101113;
  --panel:#ffffff;
  --panel-edge:#e6e2e2;
  --ink:#3b3b3f;
  --text:#4a4a4a;
  --accent:#1ebcf1;
  --accent-dark:#0a8fcf;
  --nav:#e9e9e9;
  --rule:#3c3e43;
  --muted:#8a8a8a;
}
*{box-sizing:border-box;margin:0;padding:0}
html,body{width:1200px;height:837px;overflow:hidden}
body{background:var(--bg);position:relative;font-family:"Source Sans 3",sans-serif}
.top-bar{position:absolute;left:0;top:0;width:1200px;height:13px;background:var(--accent)}
.camera-halo{position:absolute;left:70px;top:62px;width:1050px;height:695px;border-radius:70px 70px 60px 60px;background:var(--halo)}
.camera-body{position:absolute;left:82px;top:66px;width:1026px;height:676px;border-radius:60px 60px 50px 50px;
  background:radial-gradient(ellipse at 30% 20%,var(--body-mid),var(--body-dark) 70%)}
.camera-grip{position:absolute;left:300px;top:70px;width:540px;height:60px;border-radius:10px;background:linear-gradient(#2e3035,#1c1d20)}
.screen-bezel{position:absolute;left:152px;top:198px;width:627px;height:493px;border-radius:10px;background:var(--bezel)}
.screen{position:absolute;left:163px;top:205px;width:604px;height:475px;border-radius:8px;background:var(--panel);border:3px solid var(--panel-edge);padding:30px 0 0 28px;color:var(--text)}
.quote{font-family:"Signika",sans-serif;font-weight:400;font-size:24px;line-height:29px;color:var(--ink)}
.intro{font-size:13.5px;line-height:22px;margin-top:6px;width:548px;color:#444}
.gallery-title{font-family:"Signika",sans-serif;font-size:18.5px;color:var(--ink);margin:22px 0 0 3px}
.gallery{display:grid;grid-template-columns:repeat(4,106px);gap:16px 23px;margin-top:12px;list-style:none}
.thumb{width:106px;height:91px;border-radius:4px;position:relative}
.thumb .zoom{position:absolute;right:6px;bottom:5px}
.play-button{position:absolute;left:974px;top:207px;width:62px;height:62px;border-radius:50%;background:#0c0d0f;border:3px solid #3a3c41}
.play-button svg{position:absolute;left:15px;top:16px}
.brand{position:absolute;left:816px;top:296px;display:flex;align-items:center;gap:10px}
.brand-dot{width:14px;height:14px;border-radius:50%;background:#fff}
.brand-name{font-family:"Signika",sans-serif;font-weight:400;font-size:50px;color:#fff;letter-spacing:-0.5px}
.main-nav{position:absolute;left:819px;top:373px;width:172px;list-style:none}
.main-nav li{height:35.2px;border-bottom:1px solid var(--rule);display:flex;align-items:center;gap:14px;font-family:"Signika",sans-serif;font-size:17.5px;color:var(--nav)}
.main-nav li:last-child{border-bottom:none}
.main-nav li.current{color:var(--accent)}
.sign-in{position:absolute;left:816px;top:608px;width:82px;height:33px;border-radius:4px;background:linear-gradient(var(--accent),var(--accent-dark));color:#fff;font-family:"Signika",sans-serif;font-size:16px;display:flex;align-items:center;justify-content:center;border:none}
.social{position:absolute;left:912px;top:611px;display:flex;gap:4px;list-style:none}
.social li{width:25px;height:25px;border-radius:50%;background:#f2f2f2;color:#222;font-family:"Signika",sans-serif;font-size:6.5px;font-weight:600;display:flex;align-items:center;justify-content:center}
.footer-rule{position:absolute;left:0;top:774px;width:1200px;height:1px;background:#3a3a3a}
.footer{position:absolute;left:0;top:792px;width:1200px;text-align:center;font-size:12px;color:var(--muted)}
</style>
</head>
<body>
<div class="top-bar"></div>
<div class="camera-halo"></div>
<div class="camera-body" role="img" aria-label="Photograph of the back of a dark grey compact camera"></div>
<div class="camera-grip"></div>

<div class="screen-bezel"></div>
<main class="screen">
  <h1 class="quote">Imagination is everything.<br>Imagination encircles the world.- Albert Holberg</h1>
  <p class="intro">Lorem ipsum dolor sit amet, consectetuer adipiscing elit. Nam cursus. Morbi ut mi. Nullam enim leo, egestas id, condimentum at, laoreet mattis, massa. Sed eleifend nonummy diam. Praesent mauris ante, elementum et, bibendum at, posuere sit amet, nibh.</p>
  <h2 class="gallery-title">Photogallery</h2>
  <ul class="gallery">
    <li class="thumb" role="img" aria-label="Photo of a woman in a sun hat outdoors" style="background:linear-gradient(160deg,#d8d2c6,#a08a6e)"></li>
    <li class="thumb" role="img" aria-label="Photo of a wedding couple by a car" style="background:linear-gradient(160deg,#9fb3c6,#2e3035)"><svg class="zoom" width="16" height="16" viewBox="0 0 16 16"><circle cx="6.5" cy="6.5" r="4.5" fill="none" stroke="#fff" stroke-width="2"/><path d="M10 10l4.5 4.5" stroke="#fff" stroke-width="2.5"/></svg></li>
    <li class="thumb" role="img" aria-label="Photo of autumn leaves against the sun" style="background:linear-gradient(160deg,#c8402a,#f0c070)"><svg class="zoom" width="16" height="16" viewBox="0 0 16 16"><circle cx="6.5" cy="6.5" r="4.5" fill="none" stroke="#fff" stroke-width="2"/><path d="M10 10l4.5 4.5" stroke="#fff" stroke-width="2.5"/></svg></li>
    <li class="thumb" role="img" aria-label="Black and white photo of friends laughing" style="background:linear-gradient(160deg,#e4e4e4,#7a7a7a)"><svg class="zoom" width="16" height="16" viewBox="0 0 16 16"><circle cx="6.5" cy="6.5" r="4.5" fill="none" stroke="#fff" stroke-width="2"/><path d="M10 10l4.5 4.5" stroke="#fff" stroke-width="2.5"/></svg></li>
    <li class="thumb" role="img" aria-label="Photo of a hiker photographing mountains" style="background:linear-gradient(180deg,#5e7890,#6e7a3a)"></li>
    <li class="thumb" role="img" aria-label="Photo of a smiling woman" style="background:linear-gradient(160deg,#e88a66,#b25a40)"><svg class="zoom" width="16" height="16" viewBox="0 0 16 16"><circle cx="6.5" cy="6.5" r="4.5" fill="none" stroke="#fff" stroke-width="2"/><path d="M10 10l4.5 4.5" stroke="#fff" stroke-width="2.5"/></svg></li>
    <li class="thumb" role="img" aria-label="Photo of red flowers at sunset" style="background:linear-gradient(180deg,#f0a070,#b82030)"><svg class="zoom" width="16" height="16" viewBox="0 0 16 16"><circle cx="6.5" cy="6.5" r="4.5" fill="none" stroke="#fff" stroke-width="2"/><path d="M10 10l4.5 4.5" stroke="#fff" stroke-width="2.5"/></svg></li>
    <li class="thumb" role="img" aria-label="Photo of a couple sharing a secret" style="background:linear-gradient(160deg,#e8dcc8,#a0603a)"><svg class="zoom" width="16" height="16" viewBox="0 0 16 16"><circle cx="6.5" cy="6.5" r="4.5" fill="none" stroke="#fff" stroke-width="2"/><path d="M10 10l4.5 4.5" stroke="#fff" stroke-width="2.5"/></svg></li>
  </ul>
</main>

<div class="play-button"><svg width="32" height="26" viewBox="0 0 32 26"><rect x="1.5" y="1.5" width="29" height="23" fill="none" stroke="#6b8fc4" stroke-width="2.5"/><path d="M11 6.5v13l11-6.5z" fill="#6b8fc4"/></svg></div>

<div class="brand"><span class="brand-dot"></span><span class="brand-name">SnapVella</span></div>

<ul class="main-nav">
  <li class="current"><svg width="16" height="13" viewBox="0 0 16 13"><rect x="0.75" y="0.75" width="14.5" height="11.5" fill="none" stroke="#8a8c90" stroke-width="1.5"/><path d="M6 3.5v6l5-3z" fill="#8a8c90"/></svg>Home</li>
  <li><svg width="16" height="13" viewBox="0 0 16 13"><rect x="0.75" y="0.75" width="14.5" height="11.5" fill="none" stroke="#8a8c90" stroke-width="1.5"/><path d="M6 3.5v6l5-3z" fill="#8a8c90"/></svg>About</li>
  <li><svg width="16" height="13" viewBox="0 0 16 13"><rect x="0.75" y="0.75" width="14.5" height="11.5" fill="none" stroke="#8a8c90" stroke-width="1.5"/><path d="M6 3.5v6l5-3z" fill="#8a8c90"/></svg>Help</li>
  <li><svg width="16" height="13" viewBox="0 0 16 13"><rect x="0.75" y="0.75" width="14.5" height="11.5" fill="none" stroke="#8a8c90" stroke-width="1.5"/><path d="M6 3.5v6l5-3z" fill="#8a8c90"/></svg>Contact Us</li>
  <li><svg width="16" height="13" viewBox="0 0 16 13"><rect x="0.75" y="0.75" width="14.5" height="11.5" fill="none" stroke="#8a8c90" stroke-width="1.5"/><path d="M6 3.5v6l5-3z" fill="#8a8c90"/></svg>Privacy Policy</li>
  <li><svg width="16" height="13" viewBox="0 0 16 13"><rect x="0.75" y="0.75" width="14.5" height="11.5" fill="none" stroke="#8a8c90" stroke-width="1.5"/><path d="M6 3.5v6l5-3z" fill="#8a8c90"/></svg>Terms of Use</li>
</ul>

<button class="sign-in">Sign in</button>
<ul class="social">
  <li>Folk</li>
  <li>Chirp</li>
  <li>Mesh</li>
  <li>Pixo</li>
</ul>

<div class="footer-rule"></div>
<footer class="footer">© 2012 Company Name.&nbsp; All right reserved.&nbsp; Term of Use</footer>
</body>
</html>
```